Outdoor sign for Brindle Auto Restoration

I need a horizontal 4'x 8' outdoor roadside sign for my classic auto restoration business. I have uploaded colors and our logo. Needs the Brindle name, a prominent Classic AUTO RESTORATION, phone number and website. We rebuild and restore vintage cars, trucks and 4x4s. I'd like something clean but possibly retro. Classic Auto Restoration is more important than the Brindle name. It needs to be visible and readable from the street. NO CLIP ART

Target Market(s)

Customers who need their vintage care restored or upgraded. Men and women ages 25-75

Industry/Entity Type

Automotive

Colors
FFC000
F8CF3A
FAE287
FDF2CF
FEFAEE

Requirements
Must have
• Legible. Bright. Readable as a backlit 4' x 8' large horizontal sign (roughly 120cm X 240cm)
Nice to have
• Use of the Brindle logo/type, Complete or Classic before prominent AUTO RESTORATION
Should not have
• Clip art of old cars or icons. And we don't want the Brindle Logo from the website because it wont be legible from the road. I have included the Illustrator file for Brindle text in the uploads

```html
<!DOCTYPE html>
<html lang="en">
<head>
<meta charset="UTF-8">
<title>Brindle Classic Auto Restoration – Roadside Sign</title>
<link href="https://fonts.googleapis.com/css2?family=Saira+Condensed:wght@600;700;800&display=swap" rel="stylesheet">
<style>
  :root {
    --teal: #66a99b;
    --teal-light: #86bcb0;
    --teal-dark: #5a9d8f;
    --ray: rgba(255, 255, 255, 0.09);
    --amber: #f7a928;
    --white: #f7f8f6;
    --frame: rgba(255, 255, 255, 0.85);
    --web-box: rgba(78, 138, 122, 0.8);
    --car-body: #a4d8ca;
    --car-shade: #7cbcab;
  }
  html, body {
    margin: 0;
    padding: 0;
    width: 1200px;
    height: 600px;
    overflow: hidden;
    background: var(--teal);
  }
  .sign {
    position: relative;
    width: 1200px;
    height: 600px;
    overflow: hidden;
    font-family: "Saira Condensed", "Arial Narrow", sans-serif;
    background: var(--teal);
  }
  .sunburst, .frame {
    position: absolute;
    inset: 0;
  }
  .halftone-glow {
    position: absolute;
    left: 250px;
    top: 150px;
    width: 700px;
    height: 380px;
    border-radius: 50%;
    background: radial-gradient(ellipse at 50% 50%, var(--teal-light) 0%, rgba(134, 188, 176, 0.5) 45%, rgba(134, 188, 176, 0) 72%);
  }
  .brand-name {
    position: absolute;
    top: 76px;
    left: 0;
    width: 100%;
    text-align: center;
    margin: 0;
    font-size: 46px;
    font-weight: 800;
    line-height: 1;
    color: var(--amber);
    letter-spacing: 1px;
  }
  .headline {
    position: absolute;
    top: 128px;
    left: 0;
    width: 100%;
    text-align: center;
    margin: 0;
    font-size: 92px;
    font-weight: 800;
    line-height: 1;
    color: var(--white);
    letter-spacing: 2px;
    text-shadow: 0 3px 6px rgba(0, 0, 0, 0.15);
  }
  .car-photo {
    position: absolute;
    left: 232px;
    top: 228px;
    width: 722px;
    height: 200px;
    border-radius: 60px 90px 40px 40px / 50px 60px 40px 40px;
    background: linear-gradient(180deg, var(--car-body) 0%, var(--car-shade) 100%);
    box-shadow: 0 14px 22px rgba(40, 90, 78, 0.25);
  }
  .contact {
    position: absolute;
    top: 476px;
    left: 350px;
    width: 498px;
    display: flex;
    height: 42px;
    font-size: 34px;
    font-weight: 600;
    line-height: 42px;
    color: var(--white);
  }
  .contact-phone {
    background: var(--amber);
    padding: 0 13px;
    border-radius: 3px 0 0 3px;
  }
  .contact-web {
    flex: 1;
    background: var(--web-box);
    padding: 0 12px;
    border-radius: 0 3px 3px 0;
  }
</style>
</head>
<body>
  <div class="sign">
    <svg class="sunburst" width="1200" height="600" viewBox="0 0 1200 600" aria-hidden="true">
      <g fill="var(--ray)">
        <polygon points="600,300 1500,300 1486,456"/>
        <polygon points="600,300 1379,750 1289,879"/>
        <polygon points="600,300 1050,1079 908,1146"/>
        <polygon points="600,300 600,1200 444,1186"/>
        <polygon points="600,300 150,1079 21,989"/>
        <polygon points="600,300 -179,750 -246,608"/>
        <polygon points="600,300 -300,300 -286,144"/>
        <polygon points="600,300 -179,-150 -89,-279"/>
        <polygon points="600,300 150,-479 292,-546"/>
        <polygon points="600,300 600,-600 756,-586"/>
        <polygon points="600,300 1050,-479 1179,-389"/>
        <polygon points="600,300 1379,-150 1446,-8"/>
      </g>
    </svg>

    <div class="halftone-glow" role="img" aria-label="Soft halftone dot texture glowing behind the car"></div>

    <svg class="frame" width="1200" height="600" viewBox="0 0 1200 600" aria-hidden="true">
      <path d="M425 100 H80 Q61 100 61 119 V481 Q61 500 80 500 H322" fill="none" stroke="var(--frame)" stroke-width="1.5"/>
      <path d="M775 100 H1120 Q1139 100 1139 119 V481 Q1139 500 1120 500 H878" fill="none" stroke="var(--frame)" stroke-width="1.5"/>
    </svg>

    <h2 class="brand-name">BRINDLE</h2>
    <h1 class="headline">CLASSIC AUTO RESTORATION</h1>

    <div class="car-photo" role="img" aria-label="Photograph of a restored seafoam-green 1950s convertible with whitewall tyres and chrome bumpers"></div>

    <div class="contact">
      <span class="contact-phone">501 555 0142</span>
      <span class="contact-web">brindleautoworks.com</span>
    </div>
  </div>
</body>
</html>
```